Stationary for a Insurance and Investment Company
Heron Capital
Stationary for a Insurance and Investment Company - Financial Services
Creative Brief
Use same font as used in my logo
Harabara
Professional
Business Logo & Rimal Vesk, CIP, CRM
Insurance and Investment Consultant
4813 Pelbrook Lane, Suite 300, Mississauga, Ontario L4T 2K7
rimalvesk@heroncapital-example.ca
www.heroncapital-example.ca
Need to show favicons of Chatterly and Linqo+ on either front or back of business card.
Business Logo & website address (www.heroncapital-example.ca)
rimalvesk rimalvesk
Hello Designers, Please do not use transparent cards for design. I expect to see business cards, letterheads and EMAIL SIGNATURES etc. Designs submitted so far seems to be templates as all designs are similar to each other, even when they are coming from two different designers. I like to see some unique concepts. Thanks
Hello Designers, forgot to mention that favicons of Chatterly, Linqo+ and chirpet should be on either front or back of business card. Thanks

```html
<!DOCTYPE html>
<html lang="en">
<head>
<meta charset="utf-8">
<title>Heron Capital — Stationery</title>
<link rel="stylesheet" href="https://fonts.googleapis.com/css2?family=Arimo:wght@400&family=Ubuntu:wght@300;400;700&display=swap">
<style>
  :root{
    --navy:#2f3d63;
    --red:#c1343a;
    --stage:#5f5f61;
    --paper:#ffffff;
    --ink:#2b2b2b;
  }
  *{box-sizing:border-box;margin:0;padding:0}
  html,body{width:1200px;height:465px;overflow:hidden;background:var(--stage)}
  body{position:relative;font-family:"Ubuntu",sans-serif;color:var(--navy)}
  .sheet{position:absolute;background:var(--paper);overflow:hidden}
  .dark{background:var(--navy);color:#fff}
  .wave{position:absolute;left:0;width:100%;display:block}
  .wave .band{fill:var(--navy)}
  .wave .stripe{fill:var(--red)}

  /* logo lockup */
  .logo{position:absolute;display:flex;align-items:center;gap:.3em;white-space:nowrap}
  .logo-mark{width:1.15em;height:1.15em;border-radius:50%;background:var(--red);flex:none}
  .logo-name{font-family:"Ubuntu",sans-serif;font-weight:700;color:var(--navy);letter-spacing:-.02em;line-height:1}
  .logo.on-dark .logo-mark{background:#fff}
  .logo.on-dark .logo-name{color:#fff}

  /* contacts */
  .contact{position:absolute;font-weight:300;line-height:1.45}
  .contact .row{display:flex;align-items:center;gap:.5em}
  .contact.right .row{justify-content:flex-end}
  .ic{width:.9em;height:.9em;flex:none;fill:var(--red)}
  .indent{padding-left:1.4em}

  .socials{position:absolute;display:flex;gap:.12em}
  .socials span{width:1em;height:1em;border-radius:50%;background:#fff;display:block}

  /* letterhead */
  .letterhead{left:24px;top:20px;width:302px;height:426px}
  .letter{position:absolute;left:13px;top:94px;width:277px;font-family:"Arimo",sans-serif;font-size:5.7px;line-height:8.2px;color:var(--ink);text-align:justify}
  .letter p{margin-bottom:5.4px}
  .letter .date{margin-bottom:13px}
  .letter .sign{margin-top:19px}

  /* envelope */
  .env-front{left:338px;top:20px;width:346px;height:151px}
  .env-back{left:338px;top:181px;width:346px;height:150px}

  /* cards */
  .card-front{left:338px;top:343px;width:168px;height:95px}
  .card-back{left:517px;top:343px;width:168px;height:95px}
  .holder{position:absolute;right:6px;top:49px;text-align:right}
  .holder-name{font-size:7.2px;font-weight:400}
  .holder-name small{font-size:3px;font-weight:300}
  .holder-role{font-size:3px;font-weight:300}
  .spaced{position:absolute;left:0;width:100%;text-align:center;font-size:4px;font-weight:300;letter-spacing:.55em}

  /* folder */
  .folder-outer{left:697px;top:18px;width:238px;height:315px}
  .folder-inner{left:936px;top:18px;width:240px;height:315px}
  .pocket{position:absolute;top:333px;height:111px}
  .pocket path{fill:var(--red)}
</style>
</head>
<body>

<svg width="0" height="0" style="position:absolute" aria-hidden="true">
  <defs>
    <symbol id="pin" viewBox="0 0 10 10"><path d="M5 0C2.8 0 1.2 1.6 1.2 3.7 1.2 6.3 5 10 5 10s3.8-3.7 3.8-6.3C8.8 1.6 7.2 0 5 0zm0 5.2A1.5 1.5 0 1 1 5 2.2a1.5 1.5 0 0 1 0 3z"/></symbol>
    <symbol id="phone" viewBox="0 0 10 10"><path d="M3 0h4a1 1 0 0 1 1 1v8a1 1 0 0 1-1 1H3a1 1 0 0 1-1-1V1a1 1 0 0 1 1-1zm.6 1.4v5.8h2.8V1.4z"/></symbol>
    <symbol id="mail" viewBox="0 0 10 10"><path d="M0 2h10v6H0zm1 1 4 3 4-3z"/></symbol>
    <symbol id="globe" viewBox="0 0 10 10"><path d="M5 0a5 5 0 1 0 0 10A5 5 0 0 0 5 0zm0 1.5a3.5 3.5 0 0 1 0 7 3.5 3.5 0 0 1 0-7z"/></symbol>
    <symbol id="wave" viewBox="0 0 300 40" preserveAspectRatio="none">
      <path class="stripe" d="M0 2.5C70-2.5 128 7 178 19.5 128 9.5 70 2 0 6.5Z"/>
      <path class="band" d="M0 9C70 4 130 13 182 25 222 34 270 38 300 37L300 40 0 40Z"/>
      <path class="stripe" d="M188 30.5C238 35 274 33 300 28.5L300 32C274 36.5 238 37 188 30.5Z"/>
    </symbol>
  </defs>
</svg>

<!-- Letterhead -->
<section class="sheet letterhead">
  <div class="logo" style="left:13px;top:25px;font-size:17px">
    <span class="logo-mark"></span><span class="logo-name">Heron Capital</span>
  </div>
  <div class="contact" style="left:212px;top:29px;font-size:4.6px">
    <div class="row"><svg class="ic"><use href="#pin"/></svg>4813 Pelbrook Lane, Suite 300,</div>
    <div class="indent">Mississauga, Ontario L4T 2K7</div>
    <div class="row"><svg class="ic"><use href="#phone"/></svg>905-555-0148</div>
    <div class="row"><svg class="ic"><use href="#mail"/></svg>rimalvesk@heroncapital-example.ca</div>
    <div class="row"><svg class="ic"><use href="#globe"/></svg>www.heroncapital-example.ca</div>
  </div>
  <div class="letter">
    <p class="date">Tuesday, Jun 03, 2014</p>
    <p>Dear Sir,</p>
    <p>This template is designed to be used to create business letter documents that will be emailed or printed out on plain stock. Please be sure to delete all dummy text before printing our letter!</p>
    <p>Lorem ipsum dolor sit amet, consectetuer adipiscing elit. Proin vitae mauris. Fusce volutpat nunc et odio. Maecenas sapien pede, volutpat sit amet, egestas sit amet, rutrum et, lorem. Proin dictum. Nullam sit amet erat. Nulla facilisi. Morbi ut est sit amet felis euismod ullamcorper. Phasellus ac orci eget massa tincidunt scelerisque. Fusce turpis. Nam semper luctus enim.</p>
    <p>Duis convallis erat nec nisi. Integer vitae quam vel turpis blandit imperdiet. Ut urna erat, luctus eu, bibendum in, interdum et, libero. Maecenas pharetra pulvinar odio. Suspendisse ultrices, ipsum vel dignissim ornare, ante ligula eleifend enim, at viverra elit magna et urna. Fusce feugiat diam quis felis. Pellentesque laoreet nisi at lorem. Vestibulum ante ipsum primis in faucibus orci luctus et ultrices posuere cubilia Curae; Aenean tortor nulla, accumsan scelerisque, venenatis sed, consequat vel, eros. Integer cursus.</p>
    <p>Praesent vel lorem eget sem tincidunt scelerisque. Suspendisse potenti. Suspendisse condimentum eleifend purus. Vestibulum sem dui, accumsan mattis, condimentum at, aliquam quis, urna. Ut semper, magna ut tempus congue, velit odio auctor risus, nec ultricies purus lorem blandit dolor.</p>
    <p>Sincerely,</p>
    <p class="sign">The Designer</p>
  </div>
  <svg class="wave" style="top:388px;height:38px"><use href="#wave"/></svg>
  <div class="socials" style="left:15px;top:406px;font-size:8px"><span></span><span></span><span></span></div>
</section>

<!-- Envelope front -->
<section class="sheet env-front">
  <div class="logo" style="left:10px;top:17px;font-size:17px">
    <span class="logo-mark"></span><span class="logo-name">Heron Capital</span>
  </div>
  <div class="contact" style="left:12px;top:87px;font-size:5.4px">
    <div class="row"><svg class="ic"><use href="#pin"/></svg>4813 Pelbrook Lane, Suite 300,</div>
    <div class="indent">Mississauga, Ontario L4T 2K7</div>
  </div>
  <div class="contact right" style="right:13px;top:116px;font-size:5.4px">
    <div class="row">905-555-0148<svg class="ic"><use href="#phone"/></svg></div>
    <div class="row">rimalvesk@heroncapital-example.ca<svg class="ic"><use href="#mail"/></svg></div>
  </div>
  <svg class="wave" style="top:109px;height:42px"><use href="#wave"/></svg>
  <div class="contact" style="left:13px;top:131px;font-size:5.4px;color:#fff">www.heroncapital-example.ca</div>
</section>

<!-- Envelope back -->
<section class="sheet env-back">
  <svg style="position:absolute;left:0;top:0" width="346" height="60" viewBox="0 0 346 60">
    <path fill="var(--navy)" d="M0 0H346C340 20 334 33 314 36L192 52C178 54 168 54 154 52L32 36C12 33 6 20 0 0Z"/>
  </svg>
  <div class="socials" style="left:155px;top:22px;font-size:11px"><span></span><span></span><span></span></div>
</section>

<!-- Business card front -->
<section class="sheet card-front">
  <div class="logo" style="left:5px;top:12px;font-size:16px">
    <span class="logo-mark"></span><span class="logo-name">Heron Capital</span>
  </div>
  <div class="holder">
    <div class="holder-name">Rimal Vesk <small>CIP, CRM</small></div>
    <div class="holder-role">Insurance and Investment Consultant</div>
  </div>
  <div class="contact" style="left:5px;top:62px;font-size:4px">
    <div class="row"><svg class="ic"><use href="#pin"/></svg>4813 Pelbrook Lane, Suite 300,</div>
    <div class="indent">Mississauga, Ontario L4T 2K7</div>
  </div>
  <div class="contact right" style="right:6px;top:68px;font-size:4px">
    <div class="row" style="font-size:5px">905-555-0148<svg class="ic"><use href="#phone"/></svg></div>
    <div class="row">rimalvesk@heroncapital-example.ca<svg class="ic"><use href="#mail"/></svg></div>
  </div>
  <svg class="wave" style="top:72px;height:23px"><use href="#wave"/></svg>
  <div class="contact" style="left:5px;top:84px;font-size:4px;color:#fff">www.heroncapital-example.ca</div>
</section>

<!-- Business card back -->
<section class="sheet dark card-back">
  <div class="logo on-dark" style="left:42px;top:35px;font-size:12.5px">
    <span class="logo-mark"></span><span class="logo-name">Heron Capital</span>
  </div>
  <div class="spaced" style="top:64px">www.heroncapital-example.ca</div>
  <div class="socials" style="left:73px;top:75px;font-size:7px"><span></span><span></span><span></span></div>
</section>

<!-- Presentation folder, outer -->
<section class="sheet dark folder-outer">
  <div class="logo on-dark" style="left:80px;top:152px;font-size:13px;transform:translateX(-14%)">
    <span class="logo-mark"></span><span class="logo-name">Heron Capital</span>
  </div>
  <div class="socials" style="left:13px;top:285px;font-size:11px"><span></span><span></span><span></span></div>
  <div class="contact right" style="right:12px;top:277px;font-size:3.4px;color:#fff">
    <div class="row">4813 Pelbrook Lane, Suite 300,<svg class="ic"><use href="#pin"/></svg></div>
    <div class="row" style="padding-right:1.4em">Mississauga, Ontario L4T 2K7</div>
    <div class="row">905-555-0148<svg class="ic"><use href="#phone"/></svg></div>
    <div class="row">rimalvesk@heroncapital-example.ca<svg class="ic"><use href="#mail"/></svg></div>
    <div class="row">www.heroncapital-example.ca<svg class="ic"><use href="#globe"/></svg></div>
  </div>
</section>
<svg class="pocket" style="left:697px" width="238" height="111" viewBox="0 0 238 111">
  <path d="M0 0H227L201 95C197 106 190 111 178 111H0Z"/>
</svg>

<!-- Presentation folder, inner -->
<section class="sheet folder-inner">
  <div class="logo" style="left:78px;top:152px;font-size:13px;transform:translateX(-10%)">
    <span class="logo-mark"></span><span class="logo-name">Heron Capital</span>
  </div>
  <svg class="wave" style="top:285px;height:30px"><use href="#wave"/></svg>
  <div class="contact" style="left:14px;top:300px;font-size:3.6px;color:#fff">www.heroncapital-example.ca</div>
</section>
<svg class="pocket" style="left:936px" width="240" height="111" viewBox="0 0 240 111">
  <path d="M13 0H240V111H50C38 111 32 105 29 95Z"/>
</svg>

</body>
</html>
```